Bussines Card - RM EDIFICACIONES, S.A.

We need a design for a business card.
I want it to look professional, but not old fashion.
We are like "young people', somehow i want it to look fresh, new, different, but still serious and professional.
I could use, a non typical design. (I mean, not just rectangular design).

The company Name is " RM EDIFICACIONES, S.A. " we are Panamenian company (spanish language) dedicated to construction and civil engeniering.

The company logo is attached, i use it with white background. Im not sure trying different one, could try.

```html
<!DOCTYPE html>
<html lang="es">
<head>
<meta charset="utf-8">
<title>RM EDIFICACIONES, S.A. – Business Card</title>
<link href="https://fonts.googleapis.com/css2?family=Lato:wght@700&family=Questrial&display=swap" rel="stylesheet">
<style>
  :root {
    --bg: #2b2b2d;
    --card-dark: #58585c;
    --card-light: #f4f4f4;
    --ink: #3a3a3d;
    --mark: #58585c;
    --on-dark: #f2f2f2;
    --muted: #d9d9d9;
  }
  * { box-sizing: border-box; margin: 0; padding: 0; }
  html, body { width: 1200px; height: 900px; overflow: hidden; }
  body {
    background: var(--bg);
    position: relative;
    font-family: "Questrial", sans-serif;
  }
  .card {
    position: absolute;
    left: 300px;
    width: 600px;
    height: 343px;
    border-radius: 34px;
    overflow: hidden;
  }
  /* Front */
  .card-front {
    top: 90px;
    background: var(--card-dark);
    color: var(--on-dark);
    display: flex;
    flex-direction: column;
    align-items: center;
    justify-content: center;
    text-align: center;
    font-family: "Lato", sans-serif;
    font-weight: 700;
  }
  .front-square {
    width: 110px; height: 110px;
    border: 10px solid var(--on-dark);
    margin-bottom: 22px;
  }
  .front-name { font-size: 24px; letter-spacing: 4px; }
  .front-tagline { font-size: 17px; letter-spacing: 3px; margin-top: 28px; color: var(--muted); }
  /* Back */
  .card-back {
    top: 470px;
    background: var(--card-light);
    color: var(--ink);
  }
  .person { position: absolute; left: 66px; top: 52px; }
  .person-name { font-family: "Lato", sans-serif; font-weight: 700; font-size: 22px; letter-spacing: 1px; }
  .person-role { font-size: 15px; margin-top: 2px; }
  .brand {
    position: absolute; right: 50px; top: 40px;
    display: flex; flex-direction: column; align-items: center;
  }
  .brand-square { width: 86px; height: 86px; border: 9px solid var(--mark); margin-bottom: 14px; }
  .brand-name { font-family: "Lato", sans-serif; font-weight: 700; font-size: 17px; letter-spacing: 3px; color: var(--mark); }
  .icon-tab {
    position: absolute; left: 0; top: 168px;
    width: 42px; height: 175px;
    background: var(--mark);
    border-top-right-radius: 12px;
    display: flex; flex-direction: column; align-items: center;
    justify-content: space-around; padding: 10px 0;
  }
  .icon-tab svg { width: 22px; height: 22px; fill: var(--card-light); }
  .contact {
    position: absolute; left: 66px; top: 176px;
    list-style: none; font-size: 15px; line-height: 1.25;
  }
  .contact li { margin-bottom: 12px; }
  .base-band {
    position: absolute; right: 0; bottom: 0;
    width: 280px; height: 12px;
    background: var(--mark);
    border-top-left-radius: 12px;
  }
</style>
</head>
<body>

<section class="card card-front">
  <div class="front-square"></div>
  <div class="front-name">RM EDIFICACIONES</div>
  <div class="front-tagline">CONSTRUCTION &amp; CIVIL ENGENIERING</div>
</section>

<section class="card card-back">
  <div class="person">
    <div class="person-name">YOUR NAME</div>
    <div class="person-role">Designation</div>
  </div>

  <div class="brand">
    <div class="brand-square"></div>
    <div class="brand-name">RM EDIFICACIONES</div>
  </div>

  <div class="icon-tab">
    <svg viewBox="0 0 24 24" aria-label="Teléfono"><path d="M3 9c0-3 4-5 9-5s9 2 9 5v2h-5V9c-1-1-7-1-8 0v2H3zM6 12h12l2 8H4z"/></svg>
    <svg viewBox="0 0 24 24" aria-label="Móvil"><path d="M7 2h10a2 2 0 0 1 2 2v16a2 2 0 0 1-2 2H7a2 2 0 0 1-2-2V4a2 2 0 0 1 2-2zm0 3v13h10V5z"/></svg>
    <svg viewBox="0 0 24 24" aria-label="Correo"><path d="M2 5h20v14H2zm2 2v.5l8 6 8-6V7l-8 6z"/></svg>
    <svg viewBox="0 0 24 24" aria-label="Dirección"><path d="M12 2a7 7 0 0 1 7 7c0 5-7 13-7 13S5 14 5 9a7 7 0 0 1 7-7zm0 4a3 3 0 1 0 0 6 3 3 0 0 0 0-6z"/></svg>
  </div>

  <ul class="contact">
    <li>471-3360</li>
    <li>471-3360-2714</li>
    <li>info@rmedifica.com</li>
    <li>Calle 58, Bella Vista,<br>Plaza Norte, 2do Piso Local 4</li>
  </ul>

  <div class="base-band"></div>
</section>

</body>
</html>
```